Medical Office Needs an Updated Treatment Brochure

We need an updated brochure for a new treatment our offices are offering. The old brochure attached has all the current information on it, it just needs a new design.
We would like the updated version to be more modern and sleek as well as engaging.
Please see the old brochure attached for reference as well as this link: http://www.glimravex.com/medspa/iv-therapy/#1
The content from the attached brochure will remain.
UPDATE**** PLEASE SEE THE ATTACHED EXAMPLE BROCHURE OF THE DESIGN WE ARE LOOKING FOR!!
Thank you!!
Medical

```html
<!DOCTYPE html>
<html lang="en">
<head>
<meta charset="utf-8">
<title>Glimravex – IV Nutrient Therapy Brochure</title>
<link href="https://fonts.googleapis.com/css2?family=Oswald:wght@400;500&family=Arimo:wght@400;700&display=swap" rel="stylesheet">
<style>
:root{
  --green:#98cb94;
  --green-deep:#6fb06c;
  --charcoal:#4b4b4d;
  --ink:#2f2f31;
  --white:#ffffff;
  --rose:#e0567c;
  --page:#ffffff;
}
*{box-sizing:border-box;margin:0;padding:0}
html,body{width:937px;height:1200px;overflow:hidden;background:var(--page)}
body{position:relative;font-family:'Arimo',Arial,sans-serif;color:var(--ink)}
.sheet{position:absolute;left:104px;width:735px;height:520px;overflow:hidden;background:var(--white)}
.sheet--inside{top:67px}
.sheet--outside{top:628px}
.panel{position:absolute;top:0;width:245px;height:520px;overflow:hidden}
.panel--1{left:0}.panel--2{left:245px}.panel--3{left:490px}
.bg-green{background:var(--green)}
.bg-dark{background:var(--charcoal);color:var(--white)}
.heading{position:absolute;font-family:'Oswald',sans-serif;font-weight:500;font-size:15px;letter-spacing:.3px;color:var(--ink)}
.tab{position:absolute;font-family:'Arimo',Arial,sans-serif;font-weight:700;font-size:7px;letter-spacing:.2px;text-transform:uppercase;padding:3px 9px;color:var(--white);background:var(--charcoal);line-height:1.2}
.tab--green{background:var(--green);color:var(--ink)}
.copy{position:absolute;font-size:6.6px;line-height:1.5}
.copy p{margin-bottom:7px}
.copy b{font-weight:700}
.photo{position:absolute}
.offer{position:absolute;left:18px;top:376px;width:220px;display:grid;grid-template-columns:1fr 1fr;row-gap:11px}
.offer li{list-style:none;display:flex;align-items:center;gap:6px;font-size:7px;text-transform:uppercase;color:var(--white)}
.offer .dot{width:22px;height:22px;border-radius:50%;background:#e9e9e9;border:2px solid #6a6a6c}
.quote{position:absolute;border-radius:8px;font-style:italic;font-size:6.6px;line-height:1.45;padding:10px 16px 10px 26px}
.quote--green{background:var(--green);color:var(--ink)}
.quote--dark{background:var(--charcoal);color:var(--white)}
.qmark{position:absolute;font-family:'Oswald',sans-serif;font-weight:500;font-size:28px;line-height:1}
.contact{position:absolute;left:28px;top:364px;font-size:6.8px;line-height:1.4}
.contact .name{color:var(--rose);font-weight:700;text-transform:uppercase}
.contact .block{margin-bottom:9px}
.contact .line{display:flex;align-items:center;gap:10px;margin-bottom:6px}
.contact .ico{width:12px;height:12px;border-radius:50%;background:var(--green)}
.brand{position:absolute;left:16px;top:368px;width:215px}
.brand .name{display:flex;align-items:center;gap:8px;font-family:'Arimo',Arial,sans-serif;font-size:30px;font-weight:400;color:var(--green-deep);letter-spacing:-.5px}
.brand .name i{display:block;width:14px;height:14px;border-radius:50%;background:var(--rose)}
.brand .sub{font-size:5.5px;color:var(--rose);letter-spacing:.2px;margin-top:2px;text-transform:uppercase}
.title{position:absolute;left:16px;top:438px;width:215px;border-top:1px solid #bbb;padding-top:8px}
.title h1{font-family:'Oswald',sans-serif;font-weight:500;font-size:22px;letter-spacing:.2px;color:var(--ink)}
.title p{font-size:7px;text-transform:uppercase;color:#555;margin-top:2px;letter-spacing:.2px}
svg.wave{position:absolute;left:0;width:100%}
</style>
</head>
<body>

<section class="sheet sheet--inside" aria-label="Inside spread">
  <div class="panel panel--1 bg-green">
    <h2 class="heading" style="left:22px;top:22px">INGREDIENTS</h2>
    <span class="tab" style="left:8px;top:54px">What's in it?</span>
    <div class="copy" style="left:22px;top:78px;width:200px">
      <p>A number of nutrients play well-defined roles in the maintenance of a robust immune response, optimal energy, and overall health.</p>
    </div>
    <span class="tab" style="left:8px;top:126px;width:226px">Some of the amazing vitamins we use:</span>
    <div class="copy" style="left:22px;top:156px;width:200px">
      <p><b>Magnesium:</b> Many people are lacking in this essential mineral. Magnesium is an excellent therapy for patients with heart disease, respiratory problems, migraines, and more. It helps with arrhythmias and can arrest an acute asthma attack. IV magnesium is also very relaxing, something we could all use.</p>
      <p><b>Vitamin C:</b> IV administration fights off foreign invaders in your body and acts as a potent anti-histamine. From infections to cancer, the evidence of its powerful influence is simply astonishing when administered IV and in doses far too high for oral intake.</p>
      <p><b>Glutathione:</b> This is the major super-antioxidant and detoxifying agent of our body. It cannot be taken orally but is made in the body. Whey protein and other nutritionals can help build glutathione in the body. It is severely depleted by mercury and chemicals. Many people exist with glutathione deficiency.</p>
    </div>
    <svg class="wave" style="top:410px;height:110px" viewBox="0 0 245 110" preserveAspectRatio="none" aria-hidden="true">
      <path d="M0 30 Q120 -10 245 80 L245 110 L0 110Z" fill="#3c3c3e"/>
      <path d="M0 60 Q110 30 215 110 L0 110Z" fill="#6a6a6c"/>
      <path d="M0 88 Q70 78 130 110 L0 110Z" fill="var(--green)"/>
    </svg>
  </div>

  <div class="panel panel--2 bg-dark">
    <div class="photo" role="img" aria-label="Photo of a smiling couple talking outdoors on a sunny field beside an IV drip with fresh fruit" style="left:0;top:0;width:245px;height:220px;background:linear-gradient(160deg,#d7e6f2 0%,#a8c48a 55%,#6e8f4a 100%)"></div>
    <span class="tab tab--green" style="left:10px;top:229px">Our therapeutic suite</span>
    <div class="copy" style="left:16px;top:250px;width:215px;color:var(--white)">
      <p>When you receive treatment with IV nutrients, you sit comfortably in a recliner while a sterile IV line is started and your specific composition of nutrients is infused. During this time, which usually lasts less than 50 minutes, you may opt for Plug in you PDA or LapTop and go to work, read, watch TV, nap, or simply relax. A complete treatment course often requires a series of IV infusions.</p>
    </div>
    <span class="tab tab--green" style="left:10px;top:349px">What we offer</span>
    <ul class="offer">
      <li><span class="dot"></span>Glamour</li>
      <li><span class="dot"></span>Energy</li>
      <li><span class="dot"></span>Immunity</li>
      <li><span class="dot"></span>Hydration</li>
      <li><span class="dot"></span>Weight loss</li>
      <li><span class="dot"></span>Detox</li>
      <li><span class="dot"></span>Hangover</li>
      <li><span class="dot"></span>Glutathione</li>
    </ul>
  </div>

  <div class="panel panel--3">
    <span class="qmark" style="left:22px;top:26px;color:var(--charcoal)">&ldquo;</span>
    <div class="quote quote--green" style="left:22px;top:38px;width:180px">&ldquo;...Super doses can be administered via IV without gastrointestinal side effects...&rdquo;</div>
    <span class="qmark" style="left:165px;top:86px;color:var(--charcoal)">&rdquo;</span>
    <h2 class="heading" style="left:22px;top:116px">WHY IT'S BENEFICIAL</h2>
    <span class="tab tab--green" style="left:10px;top:150px;width:152px">Directly to the source</span>
    <div class="copy" style="left:22px;top:172px;width:200px">
      <p>When vitamins, minerals, and other nutrients are infused intravenously (IV) they go directly into your bloodstream to fuel your cells. That means they avoid the potential loss of potency and poor absorption in the gastrointestinal (GI) tract that is a characteristic of nutrients taken orally. This makes IV nutrient administration a powerful therapy for numerous health concerns. In addition, Super doses can be administered via IV without gastrointestinal side effects, which can limit dosing. A perfect example of this is vitamin C, which can only be taken in fairly small amounts orally before causing stomach upset. In contrast, Super doses of vitamin C, which can be very beneficial for the immune system, can be administered safely and without stomach side effects with an intravenous delivery route.</p>
    </div>
    <span class="tab tab--green" style="left:10px;top:370px;width:198px">Use IV therapy to optimize<br>your health</span>
    <div class="copy" style="left:22px;top:410px;width:200px">
      <p><b>Proactive:</b> Even if you're healthy, IV administration of a wide range of vitamins and minerals is an extremely effective way to boost your nutritional status, accelerate your athletic performance and prevent illness. It is especially important when flu season is around, or before and during stressful situations.</p>
    </div>
  </div>
</section>

<section class="sheet sheet--outside" aria-label="Outside spread">
  <div class="panel panel--1">
    <div style="position:absolute;left:0;top:320px;width:245px;height:200px;background:var(--green)"></div>
    <h2 class="heading" style="left:18px;top:26px">THE FACTS</h2>
    <span class="tab" style="left:8px;top:58px">What is IV therapy?</span>
    <div class="copy" style="left:18px;top:82px;width:195px">
      <p>IV Nutrient Therapy involves the direct administration of vital minerals, nutrients and vitamins directly into the bloodstream (intravenously infused) through an IV drip.</p>
      <p>These essential nutrients can help boost immune function, increase energy levels, assist in weight management, avoid chronic health issues, and even aid in skin rejuvenation.</p>
    </div>
    <div class="photo" role="img" aria-label="Photo of a group of smiling medical staff in scrubs and white coats" style="left:0;top:204px;width:245px;height:135px;background:linear-gradient(180deg,#f3f0ec 0%,#d8c4b4 45%,#8fb0c8 100%)"></div>
    <svg class="wave" style="top:310px;height:60px" viewBox="0 0 245 60" preserveAspectRatio="none" aria-hidden="true">
      <path d="M0 12 Q120 38 245 8 L245 60 L0 60Z" fill="var(--green)"/>
      <path d="M0 20 Q120 44 245 16" fill="none" stroke="var(--green-deep)" stroke-width="2"/>
    </svg>
    <span class="qmark" style="left:30px;top:386px;color:var(--charcoal)">&ldquo;</span>
    <div class="quote quote--dark" style="left:30px;top:398px;width:182px">&ldquo;IV Therapy is great for boosting health and preventing illness.&rdquo;</div>
    <span class="qmark" style="left:184px;top:430px;color:var(--charcoal)">&rdquo;</span>
    <svg class="wave" style="top:470px;height:50px" viewBox="0 0 245 50" preserveAspectRatio="none" aria-hidden="true">
      <path d="M0 0 Q140 30 245 50 L0 50Z" fill="var(--green-deep)"/>
    </svg>
  </div>

  <div class="panel panel--2">
    <div class="photo" role="img" aria-label="Decorative dark teal tiled pattern" style="left:0;top:0;width:245px;height:310px;background:radial-gradient(circle at 40% 35%,#1d5a60 0%,#0e2d33 45%,#05090b 100%)"></div>
    <div class="contact">
      <div class="block"><div class="name">Glimravex</div>2715 Harlow Parkway Fenmore CA 93401</div>
      <div class="block"><div class="name">Glimravex Southwest</div>8830 Larkin Avenue, Suite 410 Fenmore,<br>CA 93402</div>
      <div class="line"><span class="ico"></span>www.glimravex.com</div>
      <div class="line"><span class="ico"></span>appointments@glimravex.com</div>
      <div class="line"><span class="ico"></span>844-Glimravex</div>
    </div>
  </div>

  <div class="panel panel--3">
    <div class="photo" role="img" aria-label="Close-up photo of an IV drip chamber with a blurred blue background" style="left:0;top:0;width:245px;height:300px;background:linear-gradient(150deg,#c9d6e0 0%,#7f9ab8 45%,#3d5d8c 75%,#b7a6d8 100%)"></div>
    <div class="brand">
      <div class="name"><i></i>Glimravex</div>
      <div class="sub">Cosmetic surgery and medical aesthetics</div>
    </div>
    <div class="title">
      <h1>IV NUTRIENT THERAPY</h1>
      <p>Rentalize, recharge and rejuvenate!</p>
    </div>
  </div>

  <svg class="wave" style="left:245px;top:240px;width:490px;height:110px" viewBox="0 0 490 110" preserveAspectRatio="none" aria-hidden="true">
    <path d="M0 80 Q120 10 250 60 T490 20 L490 110 L0 110Z" fill="var(--green)"/>
    <path d="M0 98 Q140 40 270 80 T490 50 L490 110 L0 110Z" fill="var(--white)"/>
    <path d="M0 86 Q130 25 260 70 T490 34" fill="none" stroke="var(--green-deep)" stroke-width="2"/>
  </svg>
</section>

</body>
</html>
```